Barrister Letterhead incorporating existing logo/design

Require new letterhead template to incorporate logo and information on 'Letter 2015' word document. Currently the information on the letterhead is very busy and would like a cleaner look.
Must look good in black and white, and colour when printed.

Target Market(s)

Professional

Industry/Entity Type

Legal

Requirements
Must have
• Clean professional look.

```html
<!DOCTYPE html>
<html lang="en">
<head>
<meta charset="utf-8">
<title>Harlow Chambers Letterhead</title>
<link rel="stylesheet" href="https://fonts.googleapis.com/css2?family=Open+Sans:wght@600&display=swap">
<style>
  :root {
    --ink: #2b2b2b;
    --paper: #ffffff;
    --green-bright: #6fd43a;
    --green-mid: #1f8f1a;
    --green-deep: #0a3d08;
    --black: #000000;
  }
  * { margin: 0; padding: 0; box-sizing: border-box; }
  html, body { width: 728px; height: 1200px; overflow: hidden; background: var(--paper); }
  .letterhead { position: relative; width: 728px; height: 1200px; background: var(--paper); }

  .side-artwork {
    position: absolute; left: 0; top: 0; width: 178px; height: 1200px;
    background:
      linear-gradient(90deg, rgba(0,0,0,0) 0%, rgba(0,0,0,0) 30%, rgba(0,0,0,0.85) 70%, var(--black) 100%),
      linear-gradient(180deg, var(--green-bright) 0%, var(--green-mid) 45%, var(--green-deep) 100%);
  }

  .masthead { position: absolute; left: 190px; top: 24px; }
  .firm-name {
    font-family: "Open Sans", sans-serif; font-weight: 600;
    font-size: 34px; line-height: 40px;
    color: var(--ink); white-space: nowrap;
  }
  .firm-tagline {
    margin-top: 6px;
    font-family: "Open Sans", sans-serif; font-weight: 600;
    font-size: 18px; line-height: 24px;
    color: var(--ink); white-space: nowrap;
  }

  .details {
    position: absolute; top: 124px;
    font-family: "Open Sans", sans-serif; font-weight: 600;
    font-size: 9.6px; line-height: 13.6px; color: var(--ink);
    list-style: none; white-space: nowrap;
  }
  .details--address { left: 190px; }
  .details--contact { left: 470px; }

  .letter-date {
    position: absolute; left: 195px; top: 238px;
    font-family: "Open Sans", sans-serif; font-weight: 600;
    font-size: 10px; color: var(--ink);
  }
</style>
</head>
<body>
  <main class="letterhead">
    <div class="side-artwork" role="img" aria-label="Sweeping bright green light ribbons curving down a black band"></div>

    <header class="masthead">
      <div class="firm-name">HARLOW CHAMBERS</div>
      <div class="firm-tagline">Barristers and Mediators</div>
    </header>

    <ul class="details details--address">
      <li>Barrister- At-Law LL.B.</li>
      <li>ABN 51 708 264 119</li>
      <li>HARLOW CHAMBERS</li>
      <li>LEVEL 1 48 HARLOW STREET, ASHFORD</li>
      <li>P.O. BOX 212, ASHFORD. Q. 4870</li>
    </ul>

    <ul class="details details--contact">
      <li>TELEPHONE 07 4700 1288</li>
      <li>FAX 07 4700 1299</li>
      <li>Email jmarsh@harlowbar.com.au</li>
      <li>www.harlowchambers.com.au</li>
    </ul>

    <p class="letter-date">6 November 2015</p>
  </main>
</body>
</html>
```